I am looking for a poster design with a pledge for my clients to take. The pledge will be to not use tanning beds. Our company is a Spray Tanning Salon that focuses on educating our clients on the dangers of indoor tanning while offering a safe alternative through spray tanning. I have an outline of a possible wording but I am VERY open to adjustments on it!
This is not a promotional poster. This is a poster that will be hanging in the salon and our clients will sign around the wall.
Updates

Project Deadline Extended Reason: Not currently in love with any submissions and would like to see more. Looking for a more simple design overall. Added Friday, October 28, 2016

Target Market(s)

Women 20-30 years old

Industry/Entity Type

Salon

Font styles to use
Sans Serif

Requirements
Must have
• Take the pledge to ditch the bed!
• Maple Row Bronzing
• **Overall simple design, yet eye catching is requested. Not so busy**
Nice to have
• I am open to different wording!
• I pledge to be timeless
• -UVA rays in tanning beds cause wrinkles and other signs of premature aging
• I pledge to be fearless
• -Using tanning beds can cause severe eye damage, a weakened immune system, and melanoma the deadliest form of skin cancer.
• I pledge to be Sunless!
• -Join the GlowKind revolution at Maple Row Bronzing, Grand Rapids first Sunless Spa Experience.
Should not have
• The photo of the salon on it. I included that photo simply for reference of design, this is where this poster will be hung.

```html
<!DOCTYPE html>
<html lang="en">
<head>
<meta charset="utf-8">
<title>I pledge to be timeless — Maple Row Bronzing</title>
<link rel="stylesheet" href="https://fonts.googleapis.com/css2?family=Anton&family=Oswald:wght@600&display=swap">
<style>
  :root {
    --ground: #d8622f;
    --paper: #c95a2a;
    --paper-shade: #b04d22;
    --ink: #2a0a06;
    --scorch: #1e0803;
    --light: #ffffff;
  }
  html, body {
    margin: 0;
    padding: 0;
    overflow: hidden;
  }
  .poster {
    position: relative;
    width: 900px;
    height: 1200px;
    background: var(--ground);
    overflow: hidden;
    font-family: "Anton", "Arial Narrow", sans-serif;
    color: var(--ink);
  }
  .paper-sheet {
    position: absolute;
    inset: 0;
    width: 900px;
    height: 1200px;
  }
  .headline {
    position: absolute;
    left: 0;
    width: 912px;
    top: 40px;
    margin: 0;
    text-align: center;
    font-size: 176px;
    line-height: 1;
    letter-spacing: -2px;
  }
  .subhead {
    position: absolute;
    left: 0;
    width: 912px;
    top: 228px;
    margin: 0;
    text-align: center;
    font-size: 60px;
    line-height: 1;
  }
  .fact {
    position: absolute;
    left: 0;
    width: 912px;
    top: 385px;
    margin: 0;
    text-align: center;
    font-size: 54px;
    line-height: 70px;
  }
  .footer-pledge {
    position: absolute;
    left: 160px;
    width: 420px;
    top: 1113px;
    margin: 0;
    text-align: center;
    font-family: "Oswald", "Arial Narrow", sans-serif;
    font-weight: 600;
    color: var(--ink);
  }
  .footer-pledge .callout {
    display: block;
    font-size: 18px;
    line-height: 24px;
  }
  .footer-pledge .invite {
    display: block;
    font-size: 13.5px;
    line-height: 20px;
  }
  .brand-name {
    position: absolute;
    left: 688px;
    top: 1128px;
    width: 110px;
    margin: 0;
    text-align: center;
    font-family: "Oswald", "Arial Narrow", sans-serif;
    font-weight: 600;
    font-size: 14px;
    line-height: 17px;
    color: var(--light);
  }
</style>
</head>
<body>
<div class="poster">
  <svg class="paper-sheet" viewBox="0 0 900 1200" role="img" aria-label="Crumpled paper sheet with a scorched, burnt lower edge">
    <defs>
      <radialGradient id="scorch-mark" cx="0.5" cy="0.5" r="0.5">
        <stop offset="0" stop-color="var(--scorch)" stop-opacity="0.95"/>
        <stop offset="0.6" stop-color="var(--scorch)" stop-opacity="0.75"/>
        <stop offset="1" stop-color="var(--scorch)" stop-opacity="0"/>
      </radialGradient>
      <linearGradient id="paper-tone" x1="0" y1="0" x2="1" y2="1">
        <stop offset="0" stop-color="var(--paper-shade)"/>
        <stop offset="0.5" stop-color="var(--paper)"/>
        <stop offset="1" stop-color="var(--paper-shade)"/>
      </linearGradient>
    </defs>
    <path fill="url(#paper-tone)"
      d="M53 44 H847 V1000
         C835 1020 820 1040 800 1050
         C770 1062 745 1070 720 1080
         C700 1090 680 1100 660 1098
         C630 1092 600 1078 570 1080
         C540 1082 520 1095 490 1093
         C460 1090 440 1076 410 1078
         C380 1082 360 1098 330 1095
         C300 1090 285 1070 255 1072
         C225 1075 210 1092 180 1090
         C150 1088 130 1070 100 1068
         C80 1066 65 1075 53 1080 Z"/>
    <ellipse cx="800" cy="1115" rx="130" ry="90" fill="url(#scorch-mark)"/>
    <ellipse cx="690" cy="1120" rx="60" ry="45" fill="url(#scorch-mark)" opacity="0.6"/>
  </svg>

  <h1 class="headline">I pledge</h1>
  <h2 class="subhead">to be timeless</h2>
  <p class="fact">UVA rays in<br>tanning beds<br>cause wrinkles<br>and other<br>signs of<br>premature<br>aging</p>

  <p class="footer-pledge">
    <span class="callout">I pledge to be Sunless!</span>
    <span class="invite">Join the GlowKind revolution at Maple Row Bronzing,</span>
    <span class="invite">Grand Rapids first Sunless Spa Experience.</span>
  </p>

  <p class="brand-name">Maple Row Bronzing</p>
</div>
</body>
</html>
```